Forestry Industry Connection Website

We are requiring a template design that users of this system can feel comfortable with, we have attached some basic layout ideas, to point you guys in the right direction, but we need the graphic concept taken to a much higher professional level.
TimberLinkup.com plans to connect professionals and employers in the industry worldwide, we would like a design that is very easy to navigate, and reflects the green/natural/environmental nature of the industry.
We will need-
1 - A home page
2 - a dashboard page
3 - a profile page
4 - a display projects, list and details pages
5 - Most of our main menus will have sub headings, so we'll need a drop down menu design.
6 - a forum layout design
7 - chatterbook and chirpster icons integrated throughout
The logo supplied on the example designs is our final logo, so we would like the site design to complement it.
We would need the final approved designed to be coded in HTML5/CSS along with the PSD files.
UPDATE-
We have uploaded a new PDF file with a revised layout concept for the homepage, the idea keeping the most important information right at the top of the page.
also uploaded is the timber linkup logo in EPS format and some JPEG's of forest plantation.
Looking forward to seeing your design concepts.
Updates
we've added a PDF file with an idea of menus, and where info should be on the page, keeping most of the important information right at the top of the page. We have also added the TimberLinkup Logo in EPS format.

```html
<!DOCTYPE html>
<html lang="en">
<head>
<meta charset="utf-8">
<title>TimberLinkup – Home</title>
<link href="https://fonts.googleapis.com/css2?family=PT+Sans:wght@400;700&family=Open+Sans:wght@400;700&display=swap" rel="stylesheet">
<style>
:root{
  --green-deep:#0d3a1c;
  --green-dark:#1e5a1e;
  --green:#3a9a1c;
  --green-bright:#5cc02a;
  --green-text:#2a8a16;
  --lime:#9ed82a;
  --lime-dark:#6aaa12;
  --blue:#2aa0e0;
  --blue-light:#8fd4f4;
  --blue-deep:#1878c0;
  --panel-dark:#2a4424;
  --row-tint:#a9c9b8;
  --grey-line:#d4d4d4;
  --grey-bg:#dcdcdc;
  --ink:#1a1a1a;
  --white:#ffffff;
}
*{margin:0;padding:0;box-sizing:border-box}
html,body{width:751px;height:1200px;overflow:hidden;background:var(--white)}
body{position:relative;font-family:"Open Sans",Arial,sans-serif;color:var(--ink)}
.abs{position:absolute}
.heading{font-family:"PT Sans",Arial,sans-serif}

/* header */
.site-header{left:0;top:0;width:751px;height:115px;
  background:radial-gradient(ellipse 260px 70px at 330px 15px,#9ac0b0 0%,rgba(120,170,150,.4) 45%,transparent 80%),
  linear-gradient(#1a4a38 0%,#3f6e5e 40%,#d8e4de 75%,#fafcfb 100%)}
.login-label{left:446px;top:14px;font-size:9px;font-weight:700;color:var(--white)}
.login-field{top:12px;height:15px;background:var(--white);border:1px solid #8aa;font-size:8px;padding:1px 4px;color:#333}
.login-btn{left:681px;top:12px;width:47px;height:15px;border-radius:3px;background:linear-gradient(#7ef07a,#1fb23a);color:#063;font-size:8px;font-weight:700;text-align:center;line-height:15px}
.brand{left:17px;top:62px;display:flex;align-items:center;gap:8px}
.brand-dot{width:36px;height:36px;border-radius:50%;background:var(--green)}
.brand-name{font-family:"PT Sans",Arial,sans-serif;font-size:29px;font-weight:700;color:var(--green-dark);letter-spacing:-.3px}
.signup-tag{left:562px;top:52px;font-family:"PT Sans",Arial,sans-serif;font-size:14px;color:#1b2b25}
.signup-btn{left:547px;top:72px;width:173px;height:31px;border-radius:7px;background:linear-gradient(#5ccaf6,#1588d6);color:var(--white);font-family:"PT Sans",Arial,sans-serif;font-size:20px;line-height:31px;padding-left:17px}
.signup-btn svg{position:absolute;right:12px;top:6px}

/* navigation */
.main-nav{left:0;top:115px;width:751px;height:29px;background:linear-gradient(#5ab82e,#2a8a14);border-top:1px solid #8ad060;border-bottom:1px solid #1a5a0a;display:flex;padding-left:20px}
.main-nav a{display:block;color:var(--white);text-decoration:none;font-family:"PT Sans",Arial,sans-serif;font-size:13px;line-height:27px;text-align:center;border-right:1px solid #2a7a12;box-shadow:1px 0 0 #7acc4c}
.main-nav a:first-child{border-left:1px solid #2a7a12}

/* hero */
.hero{left:0;top:144px;width:751px;height:189px;background:linear-gradient(90deg,#3a5a20,#6a8a3a 25%,#4a6a28 50%,#7a9a48 75%,#3a5a22)}
.audience-card{top:162px;width:229px;height:151px;border-radius:7px;background:linear-gradient(#2ab0ec,#8fd4f4);border:1px solid #9ad8f4;color:var(--white)}
.audience-card h2{font-family:"PT Sans",Arial,sans-serif;font-weight:400;font-size:15px;padding:8px 0 0 12px;height:30px;border-bottom:1px solid rgba(255,255,255,.45)}
.audience-card ul{list-style:none;padding:7px 10px 0 12px}
.audience-card li{font-size:8px;font-weight:700;line-height:10px;margin-bottom:8px;padding-left:11px;position:relative}
.audience-card li::before{content:"»";position:absolute;left:0;top:0}
.card-actions{position:absolute;left:12px;top:119px;display:flex;align-items:center;gap:6px}
.lime-btn{border-radius:7px;background:linear-gradient(#c8f04a,#6abe16);border:1px solid #5a9a10;color:#1d3a06;font-family:"PT Sans",Arial,sans-serif;font-size:13px;height:25px;line-height:23px;padding:0 12px}
.card-or{font-family:"PT Sans",Arial,sans-serif;font-size:14px;color:#1d3a50}
.card-link{font-size:9px;font-weight:700;font-style:italic;color:#123;text-decoration:underline}

/* content shell */
.content-shell{left:14px;top:346px;width:714px;height:824px;border:2px solid var(--grey-line);border-radius:12px;background:var(--white)}
.featured{left:24px;top:357px;width:694px;height:68px;border-radius:6px;background:linear-gradient(#ececec,#cfcfcf);border:1px solid #bbb;box-shadow:0 3px 0 #bfbfbf}
.featured-title{left:38px;top:369px;font-family:"PT Sans",Arial,sans-serif;font-size:13px;color:#222}
.partner-badge{top:368px;height:42px;background:#9a9a9a;border-radius:4px;opacity:.75}

.how-it-works{left:24px;top:435px;width:694px;height:138px;border-radius:6px;background:var(--panel-dark);border:2px solid #b8c4b4}
.how-title{left:38px;top:443px;font-family:"PT Sans",Arial,sans-serif;font-size:14px;color:var(--white)}
.step-divider{top:460px;width:1px;height:105px;background:#1e331a;box-shadow:1px 0 0 #3a5a34}
.step-icon{top:470px;width:66px;height:62px}
.step-tag{top:541px;height:18px;background:var(--green);color:var(--white);font-family:"PT Sans",Arial,sans-serif;font-size:12px;line-height:18px;padding:0 14px 0 6px;clip-path:polygon(0 0,calc(100% - 9px) 0,100% 50%,calc(100% - 9px) 100%,0 100%)}

/* section boxes */
.section-box{width:339px;height:258px;border:2px solid var(--grey-line);border-radius:9px;background:var(--white)}
.section-tab{height:29px;background:linear-gradient(#3aa8e8,#1888d0);color:var(--white);font-family:"PT Sans",Arial,sans-serif;font-size:14px;line-height:29px;padding:0 28px 0 9px;clip-path:polygon(0 0,calc(100% - 6px) 0,100% 100%,0 100%)}
.section-tab svg{position:absolute;right:14px;top:9px}
.more-link{font-size:8px;font-weight:700;color:var(--ink)}
.more-link.green{color:var(--green-text);font-style:italic;font-size:9px}

.projects-table{left:28px;top:634px;width:327px;border-collapse:separate;border-spacing:0;font-size:8px;font-weight:700}
.projects-table th{background:var(--green-dark);background:linear-gradient(#2e8a16,#176a08);color:var(--white);font-size:9.5px;height:22px;text-align:left;padding-left:10px}
.projects-table th:first-child{border-radius:8px 0 0 8px}
.projects-table th:last-child{border-radius:0 8px 8px 0}
.projects-table td{height:19.8px;padding-left:6px}
.projects-table tr.tint td{background:var(--row-tint)}
.projects-table td.details{text-align:center;padding-left:0}
.projects-table .spacer td{height:5px;background:none}

.signup-list{font-size:8px;color:#222}
.signup-list h3{font-size:9.5px;font-style:italic;color:var(--green-text);margin-bottom:6px}
.signup-list ul{list-style:none;padding-left:6px;margin-bottom:12px}
.signup-list li{position:relative;padding-left:15px;line-height:15px}
.signup-list li::before{content:"↳";position:absolute;left:0;color:#555}

.about-photo{left:28px;top:900px;width:327px;height:98px;border-radius:8px;background:linear-gradient(180deg,#9ac070 0%,#4a7a2a 40%,#2e5a1c 70%,#8a7a54 100%)}
.body-copy{font-size:8px;line-height:12px;color:#222}
.testimonial-by{font-size:9.5px;font-weight:700;font-style:italic;color:var(--green-text)}

.site-footer{left:24px;top:1116px;width:694px;height:46px;border-radius:7px;background:linear-gradient(#2c6a3a,#0a3a18);color:var(--white);font-size:8px}
.footer-copy{left:14px;top:18px}
.footer-join{left:510px;top:17px;font-size:9px;font-weight:700;font-style:italic}
.social{top:13px;display:flex;align-items:center;gap:3px;font-size:7.5px;font-weight:700}
.social i{display:block;width:9px;height:9px;border-radius:2px;background:var(--white)}
</style>
</head>
<body>

<header class="abs site-header"></header>
<span class="abs login-label">Log in</span>
<div class="abs login-field" style="left:480px;width:96px">user id</div>
<div class="abs login-field" style="left:580px;width:97px">*********</div>
<div class="abs login-btn">Login</div>

<div class="abs brand"><span class="brand-dot"></span><span class="brand-name">TimberLinkup</span></div>
<div class="abs signup-tag">New to TimberLinkup</div>
<div class="abs signup-btn">SIGN UP NOW
  <svg width="19" height="19" viewBox="0 0 19 19"><circle cx="9.5" cy="9.5" r="8" fill="none" stroke="#fff" stroke-width="2"/><path d="M5 9.5h8M9.5 6l3.5 3.5L9.5 13" fill="none" stroke="#fff" stroke-width="2"/></svg>
</div>

<nav class="abs main-nav">
  <a style="width:58px">Home</a><a style="width:95px">Post Project</a><a style="width:111px">Browse Project</a><a style="width:46px">Buy</a><a style="width:48px">Sell</a><a style="width:62px">Forum</a><a style="width:58px">News</a><a style="width:59px">Share</a><a style="width:76px">About Us</a><a style="width:87px">Contact Us</a>
</nav>

<div class="abs hero" role="img" aria-label="Photo of a sunlit forest plantation"></div>

<section class="abs audience-card" style="left:21px">
  <h2>Companies</h2>
  <ul><li>Post an expression of interest and receive applications</li><li>Find Contractors World Wide</li><li>Rate Contractors after contract completion</li></ul>
  <div class="card-actions"><span class="lime-btn">Post A Project</span><span class="card-or">or</span><span class="card-link">view contractors</span></div>
</section>
<section class="abs audience-card" style="left:258px">
  <h2>Contractors</h2>
  <ul><li>Register and Search for Contracts</li><li>Global connectivity or search locally</li><li>Review automated emails for new expressions of interest</li><li>Earn Star Ratings</li></ul>
  <div class="card-actions"><span class="lime-btn">Register</span><span class="card-or">or</span><span class="card-link">browse projects</span></div>
</section>
<section class="abs audience-card" style="left:495px">
  <h2>Job Seekers</h2>
  <ul><li>Browse jobs online globally or locally</li><li>Apply for jobs online</li><li>Review automated emails for new job opportunities</li></ul>
  <div class="card-actions"><span class="lime-btn">Register</span><span class="card-or">or</span><span class="card-link">browse jobs</span></div>
</section>

<div class="abs content-shell"></div>

<div class="abs featured"></div>
<div class="abs featured-title">As Featured In</div>
<div class="abs partner-badge" style="left:186px;width:132px"></div>
<div class="abs partner-badge" style="left:346px;width:36px"></div>
<div class="abs partner-badge" style="left:426px;width:56px"></div>
<div class="abs partner-badge" style="left:516px;width:48px"></div>
<div class="abs partner-badge" style="left:608px;width:40px;border-radius:50%"></div>

<div class="abs how-it-works"></div>
<div class="abs how-title">How It Works</div>
<div class="abs step-divider" style="left:156px"></div>
<div class="abs step-divider" style="left:284px"></div>
<div class="abs step-divider" style="left:418px"></div>
<div class="abs step-divider" style="left:552px"></div>
<div class="abs step-icon" role="img" aria-label="New badge illustration" style="left:60px;background:#111;clip-path:polygon(50% 0,62% 15%,80% 8%,82% 27%,100% 33%,90% 50%,100% 67%,82% 73%,80% 92%,62% 85%,50% 100%,38% 85%,20% 92%,18% 73%,0 67%,10% 50%,0 33%,18% 27%,20% 8%,38% 15%)"></div>
<div class="abs step-icon" role="img" aria-label="Sign-in key illustration" style="left:184px;border-radius:50%;background:radial-gradient(circle at 40% 35%,#6ab0f0,#1a4ab0)"></div>
<div class="abs step-icon" role="img" aria-label="Folder with ruler illustration" style="left:316px;border-radius:5px;background:linear-gradient(#3a4a3a,#1a221a)"></div>
<div class="abs step-icon" role="img" aria-label="Open folder illustration" style="left:452px;border-radius:5px;background:linear-gradient(#ffd060,#f09a1a)"></div>
<div class="abs step-icon" role="img" aria-label="Group of people illustration" style="left:588px;border-radius:6px;background:linear-gradient(#d8a838,#7a3a8a)"></div>
<div class="abs step-tag" style="left:67px">Register</div>
<div class="abs step-tag" style="left:191px">Sign In</div>
<div class="abs step-tag" style="left:308px;padding-right:18px">Invite Project</div>
<div class="abs step-tag" style="left:442px;padding-right:18px">Selcet Project</div>
<div class="abs step-tag" style="left:567px;padding-right:18px">Complete Project</div>

<!-- recent projects -->
<div class="abs section-box" style="left:24px;top:583px"></div>
<div class="abs section-tab" style="left:19px;top:597px">Recent Projects
  <svg width="10" height="10" viewBox="0 0 10 10"><path d="M1 3v6h6M4 1h5v5M9 1L4 6" fill="none" stroke="#fff" stroke-width="1.3"/></svg></div>
<div class="abs more-link green" style="left:270px;top:610px">All Projects ····›</div>
<table class="abs projects-table">
  <tr><th style="width:156px">Project Name</th><th style="width:100px">Employer</th><th>Details</th></tr>
  <tr class="spacer"><td colspan="3"></td></tr>
  <tr class="tint"><td>Plantation new growth pruning</td><td>Ridgeline Forestry</td><td class="details">Click Here</td></tr>
  <tr><td>Seeding Transplanting</td><td>CanopyNurseries</td><td class="details">Click Here</td></tr>
  <tr class="tint"><td>Plantation new growth pruning</td><td>Ridgeline Forestry</td><td class="details">Click Here</td></tr>
  <tr><td>Seeding Transplanting</td><td>CanopyNurseries</td><td class="details">Click Here</td></tr>
  <tr class="tint"><td>Plantation new growth pruning</td><td>Ridgeline Forestry</td><td class="details">Click Here</td></tr>
  <tr><td>Seeding Transplanting</td><td>CanopyNurseries</td><td class="details">Click Here</td></tr>
  <tr class="tint"><td>Plantation new growth pruning</td><td>Ridgeline Forestry</td><td class="details">Click Here</td></tr>
  <tr><td>Seeding Transplanting</td><td>CanopyNurseries</td><td class="details">Click Here</td></tr>
  <tr class="tint"><td>Plantation new growth pruning</td><td>Ridgeline Forestry</td><td class="details">Click Here</td></tr>
</table>

<!-- sign up -->
<div class="abs section-box" style="left:379px;top:583px"></div>
<div class="abs section-tab" style="left:375px;top:597px">Sign Up Now!
  <svg width="10" height="10" viewBox="0 0 10 10"><path d="M1 3v6h6M4 1h5v5M9 1L4 6" fill="none" stroke="#fff" stroke-width="1.3"/></svg></div>
<div class="abs signup-list" style="left:387px;top:640px;width:320px">
  <h3>Companies</h3>
  <ul><li>Free 3 moths trial</li><li>Post an expression of interest and receive applications</li><li>Rate contractors after contract completion</li><li>Find contractors and employees worldwide</li></ul>
  <h3>Contractors</h3>
  <ul><li>Register and search for contractors</li><li>Earn star ratings</li><li>Receive automated emails for new expressions of interest</li><li>3 month free trail then sign for optional 6 month / 1 year subscriptions</li><li>Global connectivity or search locally</li></ul>
</div>

<!-- about -->
<div class="abs section-box" style="left:24px;top:850px"></div>
<div class="abs section-tab" style="left:19px;top:864px">About TimberLinkup
  <svg width="10" height="10" viewBox="0 0 10 10"><path d="M1 3v6h6M4 1h5v5M9 1L4 6" fill="none" stroke="#fff" stroke-width="1.3"/></svg></div>
<div class="abs about-photo" role="img" aria-label="Photo of a forest path between tall trees"></div>
<div class="abs body-copy" style="left:34px;top:1006px;width:318px">
  <p>TimberLinkup.com plans to connect people within the forestry industry, from employees to contractors aand professional worldwide.</p><br>
  <p>Currently our system hosts the most extensive database of its type anywhere, as our plans continue to expand our role in the world forestry industry is becoming widely recog-nised as an essential service.</p>
</div>
<div class="abs more-link" style="left:232px;top:1087px">More Informations ····›</div>

<!-- testimonial -->
<div class="abs section-box" style="left:379px;top:850px"></div>
<div class="abs section-tab" style="left:375px;top:864px">Testimonial
  <svg width="10" height="10" viewBox="0 0 10 10"><path d="M1 3v6h6M4 1h5v5M9 1L4 6" fill="none" stroke="#fff" stroke-width="1.3"/></svg></div>
<div class="abs body-copy" style="left:387px;top:904px;width:320px">
  <p><b>Lorem Ipsum</b> is simply dummy text of the printing and typesetting industry. Lorem Ipsum has been the industry's standard dummy text ever since the 1500s, when an unknown printer took a galley of type and scrambled it to make a type specimen book. It has survived not only five centuries, but also the leap into electronic typesetting, remaining essentially unchanged. It was popularised in the 1960s with the release of Sheetline sheets containing Lorem Ipsum passages, and more recently with desktop publishing software like Quillset Layout including versions of Lorem Ipsum.</p><br>
  <p>It was popularised in the 1960s with the release of Sheetline sheets containing Lorem Ipsum passages, and more recently with desktop publishing software like Quillset Layout including versions of Lorem Ipsum.</p>
</div>
<div class="abs testimonial-by" style="left:387px;top:1053px">Posted By Dale Morrow, CEO of Greenleaf Studio</div>
<div class="abs more-link" style="left:588px;top:1087px">More Testimonilas ····›</div>

<footer class="abs site-footer">
  <div class="abs footer-copy">© 2011, All Rights Reserved, TimberLinkup.com &nbsp; | &nbsp; Privacy Policy &nbsp; | &nbsp; Terms &amp; Conditions</div>
  <div class="abs footer-join">Join Us On</div>
</footer>
<div class="abs social" style="left:583px;top:1123px"><i></i>chatterbook</div>
<div class="abs social" style="left:642px;top:1123px"><i></i>chirpster</div>
<div class="abs social" style="left:583px;top:1141px"><i></i>feed</div>
<div class="abs social" style="left:642px;top:1141px"><i></i>linkfolio</div>

</body>
</html>
```